We need a wordpress design that will incorporate a professional color scheme with company logo in a clean layout. The design needs to consider that this will be developed on a responsive theme. Colors are red and black of the logo and and an accent color. Client wants a 'modern' look.

Industry/Entity Type

It Company

Font styles to use
Serif
Sans Serif

Colors

Designer to choose colors to be used in the design.

Requirements
Must have
• Must Have:
- Navigation: 1) Home; 2) Auctions; 3) Real Estate Listings 4) Assets For Sale 5) Services 6) About Us 7) Contact Us

Site will have slideshow - image is attached. Colors will be those in the logo, red and black with maybe an accent color. A site the client mentions liking is Brolmarket.com for the use of color and layout.

Widgets: Featured Auctions, 2) Email signup form; 3) Testimonials blog widget; 5) Featured Video; Footer will have affiliation logo and contact info.

Home page content:
We are a family owned and operated business with over 25 years of real estate experience in Clinton and surrounding areas in Western Oklahoma. We know that purchasing a home is one of the most important decisions a person can make, and we strive to make it a successful and enjoyable experience for you!
Enjoy our website and please call if you have any questions or would like to make an appointment to view property!
Also, take a moment to look at our Auction Calendar for upcoming auction dates. Auctions are a great opportunity for great deals and rare finds, not to mention A LOT OF FUN!!

Widgets: 1) Featured Properties; 2) Call to action for Sellers 3) Testimonials blog/widget
Nice to have
• use of dropdown menus

```html
<!DOCTYPE html>
<html lang="en">
<head>
<meta charset="utf-8">
<title>Pell Auction &amp; Real Estate</title>
<link href="https://fonts.googleapis.com/css2?family=Arimo:ital,wght@0,400;0,700;1,700&family=Bitter:wght@400;700&family=Oswald:wght@400;500&display=swap" rel="stylesheet">
<style>
:root{
  --red:#c41e36;
  --red-dark:#a8172c;
  --ink:#222222;
  --panel:#1f1f1f;
  --text:#333333;
  --muted:#555555;
  --light:#f2f2f2;
  --line:#dcdcdc;
  --white:#ffffff;
}
*{box-sizing:border-box;margin:0;padding:0}
html,body{width:948px;height:1200px;overflow:hidden;background:var(--white)}
body{position:relative;font-family:"Arimo",Arial,sans-serif;color:var(--text);font-size:10px}

/* header */
.site-header{position:absolute;left:0;top:0;width:948px;height:105px}
.brand{position:absolute;left:79px;top:18px;width:210px}
.brand-name{font-family:"Bitter",Georgia,serif;font-weight:700;font-size:48px;line-height:50px;color:var(--red);letter-spacing:1px}
.brand-tag{font-family:"Bitter",Georgia,serif;font-weight:400;font-size:13px;color:var(--red);margin-left:44px;margin-top:-2px}
.social{position:absolute;left:701px;top:10px;display:flex;gap:7px}
.social span{width:28px;height:28px;border-radius:50%;display:block}
.s1{background:#2e5a9a}.s2{background:#1fa3e0}.s3{background:#1a6fa8}.s4{background:#c4261d}.s5{background:#e2871e}
.callbar{position:absolute;left:611px;top:53px;width:258px;height:32px;border-bottom:1px dotted #777;display:flex;align-items:center;gap:7px}
.call-icon{width:24px;height:24px;background:var(--red);border-radius:3px;display:flex;align-items:center;justify-content:center}
.call-text{font-family:"Oswald",sans-serif;font-size:15px;color:var(--ink);letter-spacing:.2px;white-space:nowrap}
.call-text b{color:var(--red);font-weight:500;font-size:19px;margin-left:3px}

/* red stage */
.stage{position:absolute;left:0;top:105px;width:948px;height:421px;background:var(--red)}
.main-nav{position:absolute;left:79px;top:13px;width:790px;height:39px;background:var(--ink);border-radius:4px;display:flex;align-items:center;padding-left:8px}
.main-nav a{font-weight:700;font-size:11.5px;color:var(--white);text-decoration:none;padding:9px 16px;border-radius:4px;white-space:nowrap;letter-spacing:.2px}
.main-nav a.is-active{background:var(--red);padding:10px 16px}
.main-nav a:nth-child(3){margin-left:4px}
.hero{position:absolute;left:79px;top:61px;width:790px;height:338px;border:4px solid #d9d9d9;background:linear-gradient(180deg,#3f7cc7 0%,#8fb2d9 30%,#9d968e 48%,#e8e6e0 65%,#7b6a55 88%,#4d5d2e 100%)}
.dropdown{position:absolute;left:167px;top:56px;width:144px;height:90px;background:rgba(196,30,54,.85);padding:4px 4px}
.dropdown li{list-style:none;font-size:11.5px;color:var(--white);height:27px;line-height:25px;padding-left:8px;border-bottom:1px dotted rgba(255,255,255,.5)}
.dropdown li:last-child{border-bottom:0}
.dropdown li.is-current{background:var(--ink)}
.dropdown li::before{content:"»";font-weight:700;margin-right:5px}
.signup{position:absolute;left:501px;top:128px;width:270px;height:191px;background:rgba(34,34,34,.88)}
.signup-head{height:38px;background:var(--red);font-family:"Bitter",Georgia,serif;font-weight:700;font-size:16.5px;color:var(--white);padding:10px 14px;letter-spacing:.5px}
.signup p{font-size:9.5px;color:var(--white);padding:12px 16px 0;line-height:12.5px}
.field{margin:8px 0 0 15px;width:246px;height:26px;border-radius:13px;background:var(--white);font-size:10.5px;color:#444;padding:6px 13px;border:1px solid #ccc}
.btn-sub{display:inline-block;margin:9px 0 0 15px;height:25px;padding:0 8px;border-radius:13px;background:var(--white);border:2px solid var(--red);font-size:10px;font-weight:700;color:var(--ink);line-height:21px}

/* content */
.welcome{position:absolute;left:80px;top:552px;width:510px}
.welcome h1{font-family:"Bitter",Georgia,serif;font-weight:400;font-size:20.5px;color:var(--red);margin-bottom:12px}
.welcome h1 b{color:var(--ink);font-weight:700}
.welcome p{font-size:9.6px;line-height:16px;color:var(--text)}
.welcome .lead{font-style:italic;font-weight:700}
.welcome .hl{color:var(--red);font-weight:700}
.gap{height:16px}

.feature{position:absolute;width:511px;height:163px;background:var(--light);border:1px solid var(--line);border-radius:3px}
.feature h2{position:absolute;left:8px;top:7px;font-family:"Bitter",Georgia,serif;font-weight:700;font-size:17px;color:var(--red)}
.thumb{position:absolute;left:8px;top:38px;width:98px;height:72px;border:3px solid var(--white);background:linear-gradient(135deg,#2d67b7 0%,#6a9ed6 45%,#c8a77c 70%,#6b5b43 100%)}
.f-cat{position:absolute;left:124px;top:42px;font-size:11px;color:#d8293b}
.f-text{position:absolute;left:124px;top:58px;width:310px;font-size:11px;line-height:14.5px;color:#444}
.f-live{position:absolute;left:175px;top:117px;font-size:11px;color:#d8293b}
.f-small{position:absolute;left:175px;top:133px;font-size:9.5px;color:#444}
.pill{position:absolute;top:121px;height:21px;border-radius:4px;color:var(--white);font-size:9.5px;font-weight:700;display:flex;align-items:center;gap:5px;padding:0 8px}
.pill-red{left:10px;background:#e2262f;width:70px}
.pill-dark{left:88px;background:#3b3b3b;width:70px;justify-content:center}
.pill i{display:block;width:11px;height:9px;background:var(--white);border-radius:2px}

/* sidebar */
.sidebar{position:absolute;left:620px;top:553px;width:244px;height:497px;background:var(--panel);clip-path:polygon(0 0,100% 0,100% 90%,50% 100%,0 90%)}
.sidebar h3{font-family:"Bitter",Georgia,serif;font-weight:400;font-size:19.5px;color:var(--red);margin:14px 0 0 11px}
.post{position:absolute;left:14px;width:222px}
.post-thumb{position:absolute;left:0;top:2px;width:55px;height:42px;border:2px solid #ddd;background:linear-gradient(135deg,#2d67b7 0%,#6a9ed6 45%,#c8a77c 70%,#6b5b43 100%)}
.post p{margin-left:63px;font-size:9.5px;line-height:15px;color:var(--white)}
.post .more{text-align:right;color:var(--red);font-weight:700;margin-top:3px}
.divider{position:absolute;left:8px;top:208px;width:228px;border-top:1px dotted #666}
.testi{position:absolute;left:21px;top:260px;width:212px;font-size:9.5px;line-height:15px;color:var(--white);text-indent:12px}
.testi .plain{display:block;text-indent:0}
.quote{font-family:"Bitter",Georgia,serif;font-size:26px;color:#cfcfcf;position:absolute;line-height:1}
.author{position:absolute;left:0;top:414px;width:244px;text-align:center;font-size:10px;color:var(--red)}

/* footer */
.site-footer{position:absolute;left:0;top:1075px;width:948px;height:103px;background:var(--red)}
.contact{position:absolute;left:79px;top:20px;font-size:11px;line-height:17.5px;color:var(--white)}
.badges{position:absolute;left:433px;top:33px;display:flex;gap:9px;align-items:center}
.badges span{display:block;background:var(--white)}
.bottom-bar{position:absolute;left:0;top:1178px;width:948px;height:22px;background:var(--panel)}
.foot-nav{position:absolute;left:79px;top:5px;font-size:10px;color:var(--white);word-spacing:1px}
.foot-nav span{margin:0 7px}
.copy{position:absolute;right:80px;top:5px;font-size:10px;color:var(--white)}
</style>
</head>
<body>

<header class="site-header">
  <div class="brand">
    <div class="brand-name">PELL</div>
    <div class="brand-tag">Auction &amp; Real Estate</div>
  </div>
  <div class="social" aria-label="Social links">
    <span class="s1"></span><span class="s2"></span><span class="s3"></span><span class="s4"></span><span class="s5"></span>
  </div>
  <div class="callbar">
    <div class="call-icon">
      <svg width="14" height="14" viewBox="0 0 24 24"><path fill="#fff" d="M6.6 10.8c1.4 2.8 3.8 5.1 6.6 6.6l2.2-2.2c.3-.3.7-.4 1-.2 1.1.4 2.3.6 3.6.6.6 0 1 .4 1 1V20c0 .6-.4 1-1 1C10.6 21 3 13.4 3 4c0-.6.4-1 1-1h3.5c.6 0 1 .4 1 1 0 1.3.2 2.5.6 3.6.1.3 0 .7-.2 1z"/></svg>
    </div>
    <div class="call-text">CALL US TOLL-FREE ON <b>1800 552 309</b></div>
  </div>
</header>

<section class="stage">
  <nav class="main-nav">
    <a>HOME</a><a class="is-active">AUCTIONS</a><a>REAL ESTATE LISTINGS</a><a>ASSETS FOR SALE</a><a>SERVICES</a><a>ABOUT US</a><a>CONTACT US</a>
  </nav>
  <div class="hero" role="img" aria-label="Slideshow photo of a two-storey suburban house with white trim under a blue sky"></div>
  <ul class="dropdown">
    <li class="is-current">Current Auctions</li>
    <li>Past Auctions</li>
    <li>Online Auctions</li>
  </ul>
  <form class="signup">
    <div class="signup-head">EMAIL SIGN-UP</div>
    <p>Lorem ipsum dolor sit amet, ectetuer<br>&nbsp;adipiscing elit. Nam</p>
    <div class="field">First Name</div>
    <div class="field">Email address</div>
    <span class="btn-sub">Subscribe Now</span>
  </form>
</section>

<main>
  <div class="welcome">
    <h1>Welcome to <b>Pell Action &amp; Real Estate</b></h1>
    <p class="lead">Lorem Ipsum is that it has a more-or-less normal distribution of letters,</p>
    <p>as opposed to using 'Content here, content here', making it look like readable English. Many desktop publishing packages and web page editors now&nbsp; Lorem Ipsum as their default model text..</p>
    <div class="gap"></div>
    <p><span class="hl">by accident, sometimes on purpose injected humour and the likelike.</span> readable English. Many desktop pub-lishing packages and web page editors now use Lorem Ipsum.</p>
  </div>

  <article class="feature" style="left:79px;top:703px">
    <h2>Featured Auction</h2>
    <div class="thumb" role="img" aria-label="Hand holding house keys in front of a home"></div>
    <div class="f-cat">FURNITURE ‘ ANTIQUES ’ COLLECTIBLES</div>
    <div class="f-text">Lorem Ipsum is that it has a more-or-less normal distribution of letters, as opposed to using 'Content here, content here', making it look like readable English. Many desktop publish-</div>
    <span class="pill pill-red"><i></i>Details</span>
    <span class="pill pill-dark"><i></i>Photos</span>
    <div class="f-live">LIVE ON-SITE AUCTION</div>
    <div class="f-small">Lorem Ipsum is that it has a more-or-less normal distribution of letters,</div>
  </article>

  <article class="feature" style="left:80px;top:885px">
    <h2>Featured Auction</h2>
    <div class="thumb" role="img" aria-label="Hand holding house keys in front of a home"></div>
    <div class="f-cat">FURNITURE ‘ ANTIQUES ’ COLLECTIBLES</div>
    <div class="f-text">Lorem Ipsum is that it has a more-or-less normal distribution of letters, as opposed to using 'Content here, content here', making it look like readable English. Many desktop publish-</div>
    <span class="pill pill-red"><i></i>Details</span>
    <span class="pill pill-dark"><i></i>Photos</span>
    <div class="f-live">LIVE ON-SITE AUCTION</div>
    <div class="f-small">Lorem Ipsum is that it has a more-or-less normal distribution of letters,</div>
  </article>

  <aside class="sidebar">
    <h3>News &amp; Event Blog</h3>
    <div class="post" style="top:47px">
      <div class="post-thumb" role="img" aria-label="Blog post photo of a home with keys"></div>
      <p>Lorem ipsum dolor sit amet, consc-tetur adipiscing elit, sed do eiusmod tempor incididuntmagna</p>
      <p class="more">more details...</p>
    </div>
    <div class="post" style="top:122px">
      <div class="post-thumb" role="img" aria-label="Blog post photo of a home with keys"></div>
      <p>Lorem ipsum dolor sit amet, consc-tetur adipiscing elit, sed do eiusmod tempor incididuntmagna</p>
      <p class="more">more details...</p>
    </div>
    <div class="divider"></div>
    <h3 style="position:absolute;top:212px;margin:14px 0 0 14px">Testimonials</h3>
    <span class="quote" style="left:11px;top:256px">“</span>
    <p class="testi">Lorem ipsum dolor sit amet, consectetur labore et aliquip ex ea commodo consequat. Duis aute irure dolor in reprehenderit in voluptate.velit esse cillum dolore eu fugiat nulla pariatur. anim id est laborum.<span class="plain"><br>velit esse cillum dolore eu fugiat nulla pariatur. anim id est laborum.velit esse cillum dolore eu fugiat nulla pariatur. anim id est laborum.</span></p>
    <span class="quote" style="left:206px;top:378px">”</span>
    <div class="author">MR DALE PORTER...</div>
  </aside>
</main>

<footer class="site-footer">
  <div class="contact">
    Phone: (555) 214-7730<br>
    Contacts: Pell Real Estate Auction<br>
    Email: marketing@pellrealestateauction.com<br>
    Address: 14-B Market Square E, Dunmore, TN 37000
  </div>
  <div class="badges" aria-label="Affiliations">
    <span style="width:60px;height:34px"></span>
    <span style="width:30px;height:34px"></span>
    <span style="width:36px;height:36px;border-radius:50%"></span>
    <span style="width:32px;height:34px;border-radius:50%"></span>
    <span style="width:60px;height:30px"></span>
    <span style="width:54px;height:26px"></span>
    <span style="width:100px;height:30px;background:transparent;border:2px solid #fff"></span>
  </div>
</footer>
<div class="bottom-bar">
  <div class="foot-nav">Home<span>|</span>Auctions<span>|</span>Real Estate Listings<span>|</span>Assets For Sale<span>|</span>Services<span>|</span>About Us<span>|</span>Contact Us</div>
  <div class="copy">(C) Pell Real Estate Auction 2014.</div>
</div>

</body>
</html>
```